Mosquito and outdoor pest management

The uploaded logo must be integrated as the main theme of the card. I would like it to be modern and eye catching. Maybe some backround images or light silver metallic background.
Space enough at the base for contact info to be put in- phone numbers,emails,names,website.
Space on the back for short blog and lines for hand writing..calling card.
Commercial- golf courses, schools, outdoor function properties, pre event treatments.
Residential- retirement villages, townhome complexes and general houses
Management

```html
<!DOCTYPE html>
<html lang="en">
<head>
<meta charset="utf-8">
<title>Bayline Mosquito – Business Card</title>
<link href="https://fonts.googleapis.com/css2?family=Gelasio:wght@700&family=Open+Sans:wght@400&display=swap" rel="stylesheet">
<style>
  :root {
    --ink: #111111;
    --band: #0b0b0b;
    --red: #e0242f;
    --grey: #3d3d3d;
    --paper: #ffffff;
    --backdrop: #e6e4e1;
  }
  html, body {
    margin: 0;
    padding: 0;
    width: 1200px;
    height: 892px;
    overflow: hidden;
    background: var(--backdrop);
  }
  .canvas {
    width: 1200px;
    height: 892px;
    display: flex;
    align-items: center;
    justify-content: center;
    gap: 32px;
  }
  .card {
    position: relative;
    width: 560px;
    height: 320px;
    background: var(--paper);
    box-shadow: 0 6px 18px rgba(0,0,0,0.18);
    overflow: hidden;
  }
  .card-bands {
    position: absolute;
    inset: 0;
  }
  .brand {
    position: absolute;
    left: 40px;
    top: 78px;
    display: flex;
    align-items: center;
    gap: 12px;
  }
  .brand-dot {
    width: 14px;
    height: 14px;
    border-radius: 50%;
    background: var(--red);
  }
  .brand-name {
    font-family: "Open Sans", sans-serif;
    font-weight: 400;
    font-size: 30px;
    line-height: 1;
    color: var(--grey);
  }
  .holder-name {
    position: absolute;
    left: 40px;
    top: 196px;
    font-family: "Gelasio", serif;
    font-weight: 700;
    font-size: 28px;
    color: var(--red);
  }
  .divider {
    position: absolute;
    left: 262px;
    top: 158px;
    width: 1px;
    height: 78px;
    background: var(--grey);
  }
  .contact-list {
    position: absolute;
    left: 284px;
    top: 160px;
    margin: 0;
    padding: 0;
    list-style: none;
    font-family: "Open Sans", sans-serif;
    font-size: 14px;
    color: var(--ink);
  }
  .contact-list li {
    display: flex;
    align-items: center;
    gap: 10px;
    height: 26px;
  }
  .contact-icon {
    width: 14px;
    height: 14px;
    flex: none;
  }
  .services {
    position: absolute;
    left: 52px;
    top: 34px;
    width: 440px;
  }
  .service-group + .service-group {
    margin-top: 16px;
  }
  .service-heading {
    font-family: "Gelasio", serif;
    font-weight: 700;
    font-size: 25px;
    color: var(--red);
    margin: 0;
    padding-bottom: 4px;
    border-bottom: 1.5px solid var(--red);
    width: 300px;
  }
  .service-list {
    list-style: none;
    margin: 6px 0 0 0;
    padding: 0;
    font-family: "Open Sans", sans-serif;
    font-size: 17px;
    line-height: 24px;
    color: var(--ink);
  }
</style>
</head>
<body>
<main class="canvas">

  <section class="card card-front" aria-label="Card front">
    <svg class="card-bands" width="560" height="320" viewBox="0 0 560 320" aria-hidden="true">
      <path d="M0 0 H560 V38 H320 L312 52 H0 Z" fill="var(--band)"/>
      <path d="M0 52 H312 L320 38 H560" fill="none" stroke="var(--red)" stroke-width="3"/>
      <path d="M0 286 H250 L258 274 H560 V320 H0 Z" fill="var(--band)"/>
      <path d="M0 286 H250 L258 274 H560" fill="none" stroke="var(--red)" stroke-width="3"/>
    </svg>

    <div class="brand">
      <span class="brand-dot"></span>
      <span class="brand-name">Bayline Mosquito</span>
    </div>

    <div class="holder-name">Jordan Hale</div>
    <div class="divider"></div>

    <ul class="contact-list">
      <li>
        <svg class="contact-icon" viewBox="0 0 14 14" aria-hidden="true">
          <rect width="14" height="14" rx="2" fill="var(--red)"/>
          <path d="M4.2 3.2 L5.6 3.2 L6.2 5 L5.3 5.8 C5.8 7 6.9 8.1 8.2 8.7 L9 7.8 L10.8 8.4 L10.8 9.8 C7 10.2 3.8 7 4.2 3.2 Z" fill="#fff"/>
        </svg>
        <span>061 2390 4418</span>
      </li>
      <li>
        <svg class="contact-icon" viewBox="0 0 14 14" aria-hidden="true">
          <rect width="14" height="14" rx="2" fill="var(--red)"/>
          <circle cx="7" cy="7" r="3.8" fill="none" stroke="#fff" stroke-width="1.2"/>
          <path d="M3.2 7 H10.8 M7 3.2 C5.3 5.3 5.3 8.7 7 10.8 M7 3.2 C8.7 5.3 8.7 8.7 7 10.8" fill="none" stroke="#fff" stroke-width="0.9"/>
        </svg>
        <span>www.baylinemosquito.com</span>
      </li>
      <li>
        <svg class="contact-icon" viewBox="0 0 14 14" aria-hidden="true">
          <rect width="14" height="14" rx="2" fill="var(--red)"/>
          <rect x="3" y="4.2" width="8" height="5.6" fill="none" stroke="#fff" stroke-width="1.1"/>
          <path d="M3 4.4 L7 7.6 L11 4.4" fill="none" stroke="#fff" stroke-width="1.1"/>
        </svg>
        <span>hello@baylinemosquito.com</span>
      </li>
    </ul>
  </section>

  <section class="card card-back" aria-label="Card back">
    <div class="services">
      <div class="service-group">
        <h2 class="service-heading">Commercial</h2>
        <ul class="service-list">
          <li>schools</li>
          <li>golf courses</li>
          <li>pre event treatments</li>
          <li>outdoor function properties</li>
        </ul>
      </div>
      <div class="service-group">
        <h2 class="service-heading">Residential</h2>
        <ul class="service-list">
          <li>retirement villages</li>
          <li>townhome complexes and general houses</li>
        </ul>
      </div>
    </div>
  </section>

</main>
</body>
</html>
```